Stationery Design For Specialist London law firm

We have merged two firms of London lawyers to create a new firm with a new name.

The new firms name is KR Holloway. We would like to include the description Solicitors and Advocates in the design.

We need a new design for our headed paper, business cards compliment slips etc.

The image we wish to project is fresh but not gimmicky - reliable and strong but not stuffy.

We have no strong views on font or colour this really is pretty much a blank page.

Our preference is for the name to be at the top of the page

Target Market(s)

Our clients who are individuals rather than corporate and other lawyers

Industry/Entity Type

Law Firm

Requirements
Should not have
• Legal images eg scales of justice etc

Obviously nothing childish or gimmicky

```html
<!DOCTYPE html>
<html lang="en">
<head>
<meta charset="utf-8">
<title>KR Holloway — Stationery</title>
<link rel="stylesheet" href="https://fonts.googleapis.com/css2?family=Marcellus&family=Marcellus+SC&display=swap">
<style>
  :root {
    --navy: #0c2a4a;
    --navy-mid: #1b4b78;
    --silver: #b9bdc2;
    --silver-light: #e3e5e8;
    --paper: #ffffff;
    --backdrop: #dfe1e4;
    --ink: #0c2a4a;
    --ink-soft: #3a4b5e;
  }
  * { box-sizing: border-box; margin: 0; padding: 0; }
  html, body { width: 1200px; height: 800px; overflow: hidden; }
  body {
    background: var(--backdrop);
    font-family: "Marcellus", serif;
    color: var(--ink);
    position: relative;
  }
  .sheet { position: absolute; background: var(--paper); overflow: hidden; box-shadow: 0 2px 10px rgba(0,0,0,.18); }

  /* Brand lockup */
  .brand { display: flex; flex-direction: column; }
  .brand-mark { width: 18px; height: 18px; background: var(--navy); margin-bottom: 6px; }
  .brand-name { font-family: "Marcellus", serif; font-weight: 400; color: var(--navy); line-height: 1; }
  .brand-tagline { font-family: "Marcellus SC", serif; color: var(--ink-soft); letter-spacing: .04em; margin-top: 3px; }
  .brand--light .brand-name, .brand--light .brand-tagline { color: #ffffff; }
  .brand--light .brand-mark { background: #ffffff; }
  .brand--center { align-items: center; text-align: center; }

  .band {
    background: radial-gradient(ellipse at 50% 40%, var(--navy-mid) 0%, var(--navy) 70%);
  }
  .band--top { border-bottom: 3px solid var(--silver); }
  .band--bottom { border-top: 3px solid var(--silver); }

  .contact { font-family: "Marcellus SC", serif; color: var(--ink); line-height: 1.35; }

  /* Letterhead */
  .letterhead { left: 40px; top: 75px; width: 460px; height: 660px; }
  .letterhead .brand { position: absolute; left: 36px; top: 40px; }
  .letterhead .brand-name { font-size: 36px; }
  .letterhead .brand-tagline { font-size: 11px; }
  .letterhead .contact { position: absolute; right: 36px; bottom: 62px; text-align: right; font-size: 11px; }
  .letterhead .band { position: absolute; left: 0; right: 0; bottom: 0; height: 34px; }

  /* Folder */
  .folder { left: 530px; top: 75px; width: 290px; height: 395px;
    background: radial-gradient(ellipse at 50% 55%, #ffffff 0%, var(--silver-light) 65%, #cfd2d6 100%); }
  .folder .band--top { position: absolute; left: 0; right: 0; top: 0; height: 60px; }
  .folder .band--bottom { position: absolute; left: 0; right: 0; bottom: 0; height: 66px; }
  .folder .brand { position: absolute; left: 0; right: 0; top: 150px; }
  .folder .brand-mark { width: 24px; height: 24px; margin-bottom: 10px; }
  .folder .brand-name { font-size: 38px; }
  .folder .brand-tagline { font-size: 12px; }

  /* Business cards */
  .card { left: 850px; width: 310px; height: 177px; }
  .card--front { top: 75px; }
  .card--front .brand { position: absolute; right: 20px; top: 18px; }
  .card--front .brand-mark { width: 12px; height: 12px; margin-bottom: 4px; }
  .card--front .brand-name { font-size: 22px; }
  .card--front .brand-tagline { font-size: 8px; }
  .card-person { position: absolute; left: 18px; top: 54px; }
  .card-person-name { font-family: "Marcellus SC", serif; font-size: 13px; color: var(--navy); }
  .card-person-title { font-family: "Marcellus SC", serif; font-size: 8.5px; color: var(--ink-soft); }
  .card--front .band { position: absolute; left: 0; right: 0; bottom: 0; height: 84px; border-top: 2px solid var(--silver); }
  .card--front .contact { position: absolute; left: 18px; bottom: 14px; font-size: 9px; color: #ffffff; }
  .card--back { top: 275px; }
  .card--back .band { position: absolute; inset: 0; display: flex; align-items: center; justify-content: center; }
  .card--back .brand-mark { width: 16px; height: 16px; margin-bottom: 8px; }
  .card--back .brand-name { font-size: 30px; }
  .card--back .brand-tagline { font-size: 9px; color: var(--silver); }

  /* Envelope */
  .envelope { left: 530px; top: 495px; width: 630px; height: 240px; border-radius: 10px 10px 0 0; }
  .envelope .band--top { position: absolute; left: 0; right: 0; top: 0; height: 72px;
    display: flex; align-items: center; justify-content: center; }
  .envelope .flap-mark { width: 26px; height: 26px; background: #ffffff; }
  .envelope .brand { position: absolute; left: 30px; top: 90px; }
  .envelope .brand-mark { width: 14px; height: 14px; margin-bottom: 5px; }
  .envelope .brand-name { font-size: 26px; }
  .envelope .brand-tagline { font-size: 9px; }
  .envelope .contact { position: absolute; left: 0; right: 0; bottom: 36px; text-align: center; font-size: 12px; color: var(--ink-soft); }
  .envelope .band--bottom { position: absolute; left: 0; right: 0; bottom: 0; height: 24px; }
</style>
</head>
<body>

  <section class="sheet letterhead" aria-label="Letterhead">
    <div class="brand">
      <span class="brand-mark"></span>
      <span class="brand-name">KR Holloway</span>
      <span class="brand-tagline">Solicitors and Advocates</span>
    </div>
    <address class="contact">
      A: 48 Harcourt Lane,<br>
      Suite 12 London EC4 7QP<br>
      P: +44 20 7946 0311 | F: +44 20 7946 0312<br>
      office@krholloway.example | www.krholloway.example
    </address>
    <div class="band band--bottom"></div>
  </section>

  <section class="sheet folder" aria-label="Presentation folder">
    <div class="band band--top"></div>
    <div class="brand brand--center">
      <span class="brand-mark"></span>
      <span class="brand-name">KR Holloway</span>
      <span class="brand-tagline">Solicitors and Advocates</span>
    </div>
    <div class="band band--bottom"></div>
  </section>

  <section class="sheet card card--front" aria-label="Business card, front">
    <div class="brand">
      <span class="brand-mark"></span>
      <span class="brand-name">KR Holloway</span>
      <span class="brand-tagline">Solicitors and Advocates</span>
    </div>
    <div class="card-person">
      <div class="card-person-name">Daniel Marsh</div>
      <div class="card-person-title">Attorney at Law P.C.</div>
    </div>
    <div class="band">
      <address class="contact">
        A: 48 Harcourt Lane,<br>
        Suite 12 London EC4 7QP<br>
        P: +44 20 7946 0311 | F: +44 20 7946 0312<br>
        office@krholloway.example | www.krholloway.example
      </address>
    </div>
  </section>

  <section class="sheet card card--back" aria-label="Business card, back">
    <div class="band">
      <div class="brand brand--light brand--center">
        <span class="brand-mark"></span>
        <span class="brand-name">KR Holloway</span>
        <span class="brand-tagline">Solicitors and Advocates</span>
      </div>
    </div>
  </section>

  <section class="sheet envelope" aria-label="Envelope">
    <div class="band band--top"><span class="flap-mark"></span></div>
    <div class="brand">
      <span class="brand-mark"></span>
      <span class="brand-name">KR Holloway</span>
      <span class="brand-tagline">Solicitors and Advocates</span>
    </div>
    <address class="contact">48 Harcourt Lane, Suite 12 London EC4 7QP</address>
    <div class="band band--bottom"></div>
  </section>

</body>
</html>
```